Website Banner Design Needed for Health/Medical Business

We are looking for a creative and professional set of banners for the front page of our:
1. website - lumenworthclinic.com.au and velbrooktreat.com.au and tarnmoreplus.com.au

then edit the above banners to the corrrect sizes for below
2. Our facebook pages (1 for each of the above websites)

3. Our google + pages (2 in total one for melb and syd)

4. You tube pages (1 for lumenworthclinic and 1 for velbrooktreat)

We are looking for something fresh and clean that gives the feeling of:
1. Medical (dont show pictures of doctors though - nurses are ok - just not doctors)
2. Modern because PRP is a modern medical procedure
3. Most Experienced - No other clinic in Australia has performed as many PRP treatments compared to us.
4. We offer a 100% money back guarantee as well

The banners will not be animated or using layers. they will be still banners.

We would prefer to use new stock images and will purchase them for you after you have provided some suggestions/initial drafts.

Target Market(s)

men and women from 25-65

Industry/Entity Type

Health And Wellness

Number of Pages Required

1 page

Font styles to use
Sans Serif

Requirements
Must have
• no doctor images
• nurses are ok - but no doctor images
• for the images avoid fake themed images eg. a person looking in the mirror at their hair loss = NO NO NO..... instead aim for a nurse holding a test tube or a clipboard .
• The banners need to emphasise we are the only clinic who has performed 11,000+ treatments in australia
Nice to have
• a medical feeling would be nice - but dont make it too medical. i want the viewer to associate the word TRUSTED PROVEN and RELIABLE when they view the banner.
Should not have
• as mentioned no doctor or images that look like hospital too much.
• we are a private clinic run by nurses - i have to becareful not to mislead the viewer

```html
<!DOCTYPE html>
<html lang="en">
<head>
<meta charset="utf-8">
<title>PRP Treatments Banner</title>
<link rel="stylesheet" href="https://fonts.googleapis.com/css2?family=Montserrat:ital,wght@0,400;0,700;1,400;1,500;1,700;1,800&display=swap">
<style>
  :root {
    --page-bg: #ececec;
    --brand-blue: #2c87c9;
    --deep-blue: #2f5a9e;
    --band-green: #7fe08a;
    --white: #ffffff;
    --panel-white: #f4f8fb;
    --photo-light: #eef3f6;
    --photo-mid: #cfe0ea;
    --scrub-blue: #6fb3e6;
  }
  html, body {
    margin: 0;
    padding: 0;
    width: 1200px;
    height: 533px;
    overflow: hidden;
    background: var(--page-bg);
  }
  .banner {
    position: absolute;
    left: 20px;
    top: 78px;
    width: 1160px;
    height: 377px;
    display: block;
    font-family: "Montserrat", Arial, sans-serif;
  }
  .headline-lead { fill: var(--white); font-size: 28px; font-style: italic; font-weight: 400; }
  .headline-figure { fill: var(--white); font-size: 84px; font-weight: 700; letter-spacing: -2px; }
  .headline-tail { fill: var(--white); font-size: 36px; font-style: italic; font-weight: 700; }
  .guarantee-figure { fill: var(--deep-blue); font-size: 56px; font-style: italic; font-weight: 800; letter-spacing: -2px; }
  .guarantee-sign { fill: var(--deep-blue); font-size: 30px; font-style: italic; font-weight: 500; }
  .guarantee-text { fill: var(--deep-blue); font-size: 16.5px; font-style: italic; font-weight: 500; }
  .feature-text { fill: var(--deep-blue); font-size: 17px; font-style: italic; font-weight: 500; }
</style>
</head>
<body>
<svg class="banner" viewBox="0 0 1273 414" xmlns="http://www.w3.org/2000/svg">
  <defs>
    <linearGradient id="photo-tone" x1="0" y1="0" x2="1" y2="0">
      <stop offset="0" stop-color="#e4ecf1"/>
      <stop offset="0.5" stop-color="#f3f7f9"/>
      <stop offset="1" stop-color="#dbe9ee"/>
    </linearGradient>
    <radialGradient id="nurse-tone" cx="0.5" cy="0.7" r="0.6">
      <stop offset="0" stop-color="#6fb3e6"/>
      <stop offset="0.6" stop-color="#9ccbea" stop-opacity="0.7"/>
      <stop offset="1" stop-color="#e4ecf1" stop-opacity="0"/>
    </radialGradient>
    <linearGradient id="panel-tone" x1="0" y1="0" x2="1" y2="0">
      <stop offset="0" stop-color="#ffffff"/>
      <stop offset="1" stop-color="#e9f1f7"/>
    </linearGradient>
  </defs>

  <g class="photo" role="img" aria-label="Smiling nurse in blue scrubs with a stethoscope, holding a pen, in a bright clinic room">
    <rect x="0" y="0" width="880" height="414" fill="url(#photo-tone)"/>
    <ellipse cx="270" cy="300" rx="230" ry="260" fill="url(#nurse-tone)"/>
  </g>

  <polygon class="headline-panel" points="510,0 1273,0 1273,414 860,414" fill="var(--brand-blue)"/>
  <polygon class="guarantee-panel" points="540,268 880,268 1038,414 690,414" fill="url(#panel-tone)"/>
  <polygon class="feature-band" points="0,373 660,373 690,414 0,414" fill="var(--band-green)"/>

  <text class="headline-lead" x="1203" y="68" text-anchor="end">Only Australian clinic to perform</text>
  <text class="headline-figure" x="1198" y="156" text-anchor="end">11,000+</text>
  <text class="headline-tail" x="1201" y="203" text-anchor="end">PRP Treatments</text>

  <text class="guarantee-figure" x="700" y="338">100</text>
  <text class="guarantee-sign" x="812" y="318">%</text>
  <text class="guarantee-text" x="730" y="368">Satisfaction or</text>
  <text class="guarantee-text" x="730" y="388">Money Back Guarantee</text>

  <text class="feature-text" x="38" y="399">Trained Staff</text>
  <text class="feature-text" x="173" y="399">.</text>
  <text class="feature-text" x="206" y="399">Reliable Equipment</text>
  <text class="feature-text" x="400" y="399">.</text>
  <text class="feature-text" x="424" y="399">Best Consultancy</text>
</svg>
</body>
</html>
```